lab equipment website

We need a fresh new look for a company website called tarvio. We will be using the current logo and brand colors on their current website tarvio.com. They want to keep their text and on-page SEO, but would like to reformat it to look more modern and fresh. They want to have everything be high performance with a great user experience. Their main call to action is for people to fill in a contact form so they can call them. There is some information that is purposely above the fold on the instrument pages. I will need the home page, about page and a leasing page.

```html
<!DOCTYPE html>
<html lang="en">
<head>
<meta charset="utf-8">
<title>tarvio — Lab Equipment Service Plans and Leasing</title>
<link rel="stylesheet" href="https://fonts.googleapis.com/css2?family=Montserrat:wght@300;400;500;600;700;800&display=swap">
<style>
:root{
  --teal:#1db5a9;
  --topbar:#2e2e2e;
  --ink:#2b2b2b;
  --body:#444;
  --track:#e6e6e6;
  --footer:#2c5763;
  --footer-dark:#234955;
  --white:#fff;
  --ring-light:#8fd18f;
  --ring-mid:#3f9c83;
  --ring-blue:#0e4f7a;
  --ring-core:#1d3345;
}
*{box-sizing:border-box;margin:0;padding:0}
html,body{width:1200px;height:2278px;overflow:hidden}
body{position:relative;font-family:'Montserrat',sans-serif;color:var(--body);background:var(--white)}
.abs{position:absolute}
a{color:inherit;text-decoration:none}

/* top bar */
.topbar{left:0;top:0;width:1200px;height:61px;background:var(--topbar)}
.brand{left:240px;top:14px;display:flex;align-items:center;gap:8px}
.brand-mark{width:26px;height:26px;background:var(--teal);border-radius:50%}
.brand-name{font-size:27px;font-weight:700;color:var(--white);line-height:1}
.top-contact{top:18px;display:flex;align-items:center;gap:13px;font-size:9px;font-weight:600;color:var(--white);line-height:24px}
.round-icon{width:24px;height:24px;border-radius:50%;background:var(--white);display:flex;align-items:center;justify-content:center}

/* nav */
.nav{left:0;top:61px;width:1200px;height:45px;background:var(--teal)}
.nav-item{top:14px;font-size:11.5px;font-weight:700;color:var(--white);line-height:16px}
.nav-search{left:799px;top:14px}
.search-box{left:756px;top:107px;width:112px;height:14px;border:1.5px solid #ddd;border-radius:8px;background:rgba(30,30,30,.6);font-size:7px;color:#ccc;padding-left:8px;line-height:11px}

/* hero */
.hero{left:0;top:106px;width:1200px;height:330px;background:radial-gradient(ellipse at 55% 45%,#3f8b86 0%,#1f5d5c 45%,#0f2f33 100%)}
.hero-title{left:0;top:158px;width:1200px;text-align:center;color:var(--white);font-size:29px;font-weight:800;line-height:36px;letter-spacing:.5px}
.hero-sub{left:390px;top:241px;width:420px;text-align:center;color:var(--white);font-size:8.6px;font-weight:600;line-height:19px}
.btn{display:flex;align-items:center;justify-content:center;font-size:9.5px;font-weight:700;color:var(--white);text-transform:uppercase}
.btn-solid{background:var(--teal)}
.btn-ghost{border:2px solid var(--teal)}

/* intro */
.section-title{font-weight:400;color:var(--ink)}
.intro-title{left:0;top:460px;width:1200px;text-align:center;font-size:23px;line-height:27px}
.intro-text{left:350px;top:532px;width:500px;text-align:center;font-size:8.6px;line-height:18.8px;color:#555}
.intro-text b{font-weight:600;color:var(--ink)}
.feature{top:627px;width:200px;text-align:center;font-size:12px;line-height:15px;color:var(--ink);font-weight:500}
.feature-icon{width:82px;height:82px;border:2px solid var(--teal);border-radius:50%;margin:0 auto 17px;display:flex;align-items:center;justify-content:center}
.divider{left:240px;top:800px;width:720px;height:1px;background:#eee}

/* needs */
.needs-title{left:240px;top:830px;width:440px;font-size:22px;font-weight:300;line-height:27px}
.needs-body{left:240px;top:903px;width:440px;font-size:8.6px;line-height:16px;color:#333}
.needs-body ul{list-style:none;padding-left:14px}
.needs-body .gap{margin-top:5px}
.needs-body b{font-weight:600}
.chart{left:696px;top:845px}

/* skills */
.skills-head{top:1153px;width:300px;text-align:center;font-size:15px;font-weight:600;color:var(--ink);line-height:18px}
.bar-label{font-size:10.5px;color:#555;line-height:14px}
.label-right{width:300px;left:240px;text-align:right}
.track{height:6px;background:var(--track);border-radius:3px;overflow:hidden}
.fill{position:absolute;top:0;height:6px;background:var(--teal);border-radius:3px}

/* team */
.team{left:0;top:1337px;width:1200px;height:374px;background:linear-gradient(180deg,#a8b4b6 0%,#7f8e92 45%,#3e4c52 100%)}
.card{top:1375px;width:188px;height:300px;background:var(--white)}
.card-head{height:129px;background:var(--teal);text-align:center;color:var(--white);padding-top:10px}
.avatar{width:76px;height:76px;border-radius:50%;border:3px solid var(--white);margin:0 auto 4px;background:linear-gradient(180deg,#c9c3b8,#7b7468)}
.card-name{font-size:10px;font-weight:700;line-height:14px}
.card-role{font-size:8.5px;font-weight:600;line-height:11px}
.quote{width:32px;height:32px;border-radius:50%;background:var(--teal);border:3px solid var(--white);margin:-2px auto 0;display:flex;align-items:center;justify-content:center;color:var(--white);font-size:19px;font-weight:800;line-height:1;padding-top:8px}
.card-text{padding:6px 11px 0;text-align:center;font-size:7.8px;line-height:14px;color:#333}

/* questions */
.q-mark{left:413px;top:1708px;width:374px;height:374px;border-radius:50%;background:#f5f5f5}
.q-title{left:0;top:1764px;width:1200px;text-align:center;font-size:23px;font-weight:600;color:var(--ink);line-height:30px}
.q-text{left:350px;top:1818px;width:500px;text-align:center;font-size:10px;line-height:18px;color:#444}
.q-text span{color:var(--teal)}

/* footer */
.footer{left:0;top:1960px;width:1200px;height:288px;background:var(--footer)}
.foot-title{left:0;top:1984px;width:1200px;text-align:center;font-size:16px;font-weight:700;color:var(--white);line-height:20px}
.foot-about{left:250px;top:2010px;width:700px;text-align:center;font-size:8.4px;font-weight:600;line-height:18px;color:var(--white)}
.foot-head{top:2067px;font-size:9px;font-weight:700;color:var(--white);line-height:12px}
.contact-list{left:240px;top:2094px;list-style:none;font-size:9px;font-weight:600;color:var(--white)}
.contact-list li{display:flex;align-items:flex-start;gap:10px;line-height:18px;margin-bottom:6px}
.contact-list .dot{width:16px;height:16px;border-radius:50%;background:var(--white);flex:none;margin-top:1px}
.news-text{left:480px;top:2089px;width:240px;text-align:center;font-size:9px;font-weight:600;line-height:19px;color:var(--white)}
.news-text span{color:var(--teal)}
.news-input{left:462px;top:2136px;width:188px;height:29px;border:1px solid #9bb;font-size:9.5px;color:#ccd;padding:8px;line-height:12px}
.news-btn{left:650px;top:2136px;width:90px;height:29px;text-transform:none}
.social{left:545px;top:2195px;display:flex;gap:6px}
.social span{width:22px;height:22px;border-radius:50%;background:#dfe6e8}
.quick{left:880px;top:2087px;width:81px;text-align:right;font-size:9px;font-weight:600;line-height:18.5px;list-style:none;color:var(--white)}
.bottom{left:0;top:2248px;width:1200px;height:30px;background:var(--footer-dark);font-size:8px;color:#d4dee0;padding:10px 0 0 240px;line-height:10px}
</style>
</head>
<body>

<header>
  <div class="abs topbar"></div>
  <div class="abs brand"><span class="brand-mark"></span><span class="brand-name">tarvio</span></div>
  <div class="abs top-contact" style="left:714px">
    <span class="round-icon"><svg width="12" height="9" viewBox="0 0 12 9"><rect x="0.5" y="0.5" width="11" height="8" fill="none" stroke="#2e2e2e"/><path d="M0.5 0.5 6 5 11.5 0.5" fill="none" stroke="#2e2e2e"/></svg></span>info@tarvio.com
  </div>
  <div class="abs top-contact" style="left:858px">
    <span class="round-icon"><svg width="12" height="12" viewBox="0 0 24 24"><path d="M6.6 10.8a15.1 15.1 0 0 0 6.6 6.6l2.2-2.2c.3-.3.7-.4 1-.2 1.1.4 2.3.6 3.6.6.6 0 1 .4 1 1V20c0 .6-.4 1-1 1A17 17 0 0 1 3 4c0-.6.4-1 1-1h3.5c.6 0 1 .4 1 1 0 1.3.2 2.5.6 3.6.1.3 0 .7-.2 1z" fill="#2e2e2e"/></svg></span>(555) 014-2780
  </div>

  <nav class="abs nav">
    <span class="abs nav-item" style="left:383px">HOME</span>
    <span class="abs nav-item" style="left:460px">ABOUT</span>
    <span class="abs nav-item" style="left:544px">LEASING</span>
    <span class="abs nav-item" style="left:638px">FAQ</span>
    <span class="abs nav-item" style="left:703px">CONTACT</span>
    <svg class="abs nav-search" width="16" height="16" viewBox="0 0 17 17"><circle cx="7" cy="7" r="5.5" fill="none" stroke="#fff" stroke-width="1.5"/><path d="M11 11 15.5 15.5" stroke="#fff" stroke-width="1.5"/></svg>
  </nav>
</header>

<section class="abs hero" role="img" aria-label="Laboratory photograph with microscopes and equipment under a teal tint"></section>
<div class="abs search-box">Search...</div>
<h1 class="abs hero-title">OUR GOAL IS SIMPLE<br>SAVE LABS TIME AND MONEY</h1>
<p class="abs hero-sub">tarvio is a lab support program that provides scientists with comprehensive maintenance/repair coverage and operating lease solutions at an affordable price.</p>
<a class="abs btn btn-solid" style="left:485px;top:290px;width:108px;height:37px">Contact Us</a>
<a class="abs btn btn-ghost" style="left:604px;top:290px;width:111px;height:37px">Learn More</a>

<section>
  <h2 class="abs section-title intro-title">Trusted Company Offering Scientific<br>Equipment Service Plans and Flexible Leases</h2>
  <p class="abs intro-text">At tarvio, our goal is to ensure the success of your business. Whether you are running a laboratory or other scientific facilities, we want to keep you provided with the best in cutting-edge equipment. That's why we offer flexible <b>scientific equipment leasing</b> options with worry-free service plans- to provide your business with the tools needed to perform at its peak.</p>

  <div class="abs feature" style="left:260px">
    <div class="feature-icon"><svg width="30" height="26" viewBox="0 0 30 26"><rect x="10" y="1" width="10" height="6" rx="1" fill="none" stroke="#1db5a9" stroke-width="2.5"/><rect x="1" y="6" width="28" height="19" rx="2" fill="#1db5a9"/><path d="M15 10v11M9.5 15.5h11" stroke="#fff" stroke-width="3"/></svg></div>
    Worry free lab equipment<br>PM/repair coverage
  </div>
  <div class="abs feature" style="left:498px">
    <div class="feature-icon"><svg width="26" height="32" viewBox="0 0 26 32"><rect x="8" y="1" width="6" height="14" rx="1" transform="rotate(-20 11 8)" fill="#1db5a9"/><circle cx="14" cy="19" r="6" fill="none" stroke="#1db5a9" stroke-width="2.5"/><path d="M3 30h20M8 26h10" stroke="#1db5a9" stroke-width="2.5"/></svg></div>
    Cost-effective lease<br>structures and payment<br>plans.
  </div>
  <div class="abs feature" style="left:740px">
    <div class="feature-icon"><svg width="24" height="30" viewBox="0 0 24 30"><path d="M8 1h8M9 1v10L1 27c-.5 1 .2 2 1.3 2h19.4c1.1 0 1.8-1 1.3-2L15 11V1" fill="none" stroke="#1db5a9" stroke-width="2.2"/><path d="M5 20h14l3.5 7.5H1.5z" fill="#1db5a9"/></svg></div>
    Knowledge of the<br>laboratory.
  </div>
  <div class="abs divider"></div>
</section>

<section>
  <h2 class="abs section-title needs-title">We Understand Your Needs<br>Because We Are Scientists First</h2>
  <div class="abs needs-body">
    <p>When it comes to creating innovative solutions that cater to your lab, tarvio's dedicated team of problem-solvers has got you covered. Here's how we save you time and money:</p>
    <ul class="gap">
      <li>• We collaborate with you directly- no middlemen</li>
      <li>• We handle scientific equipment service, repairs, and maintenance</li>
      <li>• We consolidate and streamline the ancillary work associated with lab equipment procurement and service</li>
      <li>• We utilize our networks to bring you the most cost-savings possible</li>
      <li>•We improve cash flow by removing the upfront cost of purchasing, freeing up capital in your everyday budget</li>
      <li>• We may provide tax advantages with our lease structures</li>
    </ul>
    <p class="gap">We regularly provide businesses with what they need to improve their budget and efficiency. We offer <b>laboratory equipment leasing</b> for a wide range of needs. If you want to discuss your needs more in-depth, don't hesitate to call us at (555) 014-2780 or fill out our <b>contact form</b>.</p>
  </div>

  <svg class="abs chart" width="264" height="264" viewBox="0 0 266 266" aria-label="Coverage rings chart">
    <circle cx="133" cy="133" r="122" fill="none" stroke="var(--ring-light)" stroke-width="14" stroke-dasharray="650 116" transform="rotate(-70 133 133)"/>
    <circle cx="133" cy="133" r="100" fill="none" stroke="var(--ring-mid)" stroke-width="18" stroke-dasharray="520 108" transform="rotate(200 133 133)"/>
    <circle cx="133" cy="133" r="79" fill="none" stroke="var(--ring-blue)" stroke-width="16"/>
    <circle cx="133" cy="133" r="70" fill="var(--ring-core)"/>
    <circle cx="133" cy="133" r="43" fill="none" stroke="#fff" stroke-width="2.5"/>
    <text x="133" y="122" text-anchor="middle" fill="#fff" font-family="Montserrat,sans-serif" font-size="10.5" font-weight="700">We have</text>
    <text x="133" y="136" text-anchor="middle" fill="#fff" font-family="Montserrat,sans-serif" font-size="10.5" font-weight="700">you completely</text>
    <text x="133" y="150" text-anchor="middle" fill="#fff" font-family="Montserrat,sans-serif" font-size="10.5" font-weight="700">covered</text>
  </svg>
</section>

<section>
  <h3 class="abs skills-head" style="left:239px">Our Skills</h3>
  <h3 class="abs skills-head" style="left:661px">The Competition</h3>

  <span class="abs bar-label label-right" style="top:1205px">Cost Saving</span>
  <div class="abs track" style="left:240px;top:1223px;width:300px"><div class="fill" style="left:18px;width:282px"></div></div>
  <span class="abs bar-label label-right" style="top:1242px">Lease Plan Flexibility</span>
  <div class="abs track" style="left:240px;top:1259px;width:300px"><div class="fill" style="left:38px;width:262px"></div></div>
  <span class="abs bar-label label-right" style="top:1280px">Customer Service</span>
  <div class="abs track" style="left:240px;top:1299px;width:300px"><div class="fill" style="left:1px;width:299px"></div></div>

  <span class="abs bar-label" style="left:660px;top:1205px">Reliability</span>
  <div class="abs track" style="left:660px;top:1223px;width:300px"><div class="fill" style="left:0;width:118px"></div></div>
  <span class="abs bar-label" style="left:660px;top:1242px">Continued Support</span>
  <div class="abs track" style="left:660px;top:1259px;width:300px"><div class="fill" style="left:0;width:89px"></div></div>
</section>

<section>
  <div class="abs team" role="img" aria-label="City skyline photograph seen from above"></div>

  <article class="abs card" style="left:240px">
    <div class="card-head"><div class="avatar" role="img" aria-label="Portrait photo of Mark Delling"></div><div class="card-name">MARK DELLING</div><div class="card-role">FINANCE</div></div>
    <div class="quote">“</div>
    <p class="card-text">tarvio's success is measured by our customers' financial savings and productivity, making your laboratory's interests our main priority. The more time and money we save you, the better we've done our job.</p>
  </article>
  <article class="abs card" style="left:506px">
    <div class="card-head"><div class="avatar" role="img" aria-label="Portrait photo of Ray Tomas"></div><div class="card-name">RAY TOMAS</div><div class="card-role">LAB RELATIONS</div></div>
    <div class="quote">“</div>
    <p class="card-text">My time spent in the lab opened my eyes to the passion and dedication that drives scientists, as well as the frustration of a tight budget and equipment upkeep. tarvio was created in order to help overcome these obstacles and enable scientists to focus on what they're truly passionate about: research.</p>
  </article>
  <article class="abs card" style="left:773px">
    <div class="card-head"><div class="avatar" role="img" aria-label="Portrait photo of Arun Kalvi"></div><div class="card-name">ARUN KALVI</div><div class="card-role">OPERATIONS</div></div>
    <div class="quote">“</div>
    <p class="card-text">The core of my involvement in tarvio extends far beyond business development. My goal is to see that researchers and scientists are provided with an effective operational solution, so that together we can be a driving force in the progress of science.</p>
  </article>
</section>

<section>
  <div class="abs q-mark"></div>
  <h2 class="abs q-title">Further questions?</h2>
  <p class="abs q-text">Feel free to contact us if you have any questions or comments. We promise to get back to you <span>within 24 hours.</span></p>
  <a class="abs btn btn-solid" style="left:544px;top:1862px;width:112px;height:37px">Contact Us</a>
</section>

<footer>
  <div class="abs footer"></div>
  <h2 class="abs foot-title">tarvio Inc.</h2>
  <p class="abs foot-about">We are a team of Westbridge University scientists driven by our passion for research. We strive to serve the scientific community. We love what we do, and who we work with. Together we can make positive changes in the world of research.</p>

  <h4 class="abs foot-head" style="left:240px">CONTACT INFO</h4>
  <ul class="abs contact-list">
    <li><span class="dot"></span><span>48 Harbor Lane<br>Suite 310<br>Bayview, CA 90000</span></li>
    <li><span class="dot"></span><span>(555) 014-2780</span></li>
    <li><span class="dot"></span><span>info@tarvio.com</span></li>
    <li><span class="dot"></span><span>https://tarvio.com</span></li>
  </ul>

  <h4 class="abs foot-head" style="left:567px">NEWSLETTER</h4>
  <p class="abs news-text">Sign up for the latest news, offers from<br><span>tarvio Inc.</span></p>
  <div class="abs news-input">Enter your email here...</div>
  <a class="abs btn btn-solid news-btn">Subscribe</a>
  <div class="abs social"><span></span><span></span><span></span><span></span></div>

  <h4 class="abs foot-head" style="left:901px">QUICK LINKS</h4>
  <ul class="abs quick">
    <li>Home</li><li>About</li><li>Leasing</li><li>FAQ</li><li>Contact</li>
  </ul>

  <div class="abs bottom">tarvio © | 2018 | All Rights Reserved.</div>
</footer>

</body>
</html>
```